Harlow Creek Church Invite Card

We are a vibrant multigenerational church outside of Raleigh, NC and are wanting a 'church invite card' that we can encourage our members to carry with them so that they can invite their friends to church.

These cards should have a modern feel (see http://zentravio.com/neat-card-ideas/ for the feel we are going for), match the branding of our website (www.harlowcreek.org) and include the following information on the back:

Service Times: Sunday @ 8:30 AM and 11:00 AM (Main Focus)
Website: www.harlowcreek.org (Main Focus)
Social Media: (You can simply use the icons for these if desired)
www.plazebook.example/harlowcreekchurch
www.snapgrove.example/harlowcreekchurch
www.vidstream.example/harlowcreekyouth
Address: 4827 Marlow Avenue Ashvale, ST 00481 (Not a main focus)
Phone: (555) 555-0182 (Not a main focus)

The front should simply say 'We look forward to meeting you!'

Logos: Attached you will find the necessary logos for this project.

Fonts and Colors: Here are the specific colors (See HCC_Website_Color_Palette.pdf) and fonts that are used on our website.
Pacifico
Helvetica
Open Sans Regular

Target Market(s)

Friends of our congregation

Industry/Entity Type

Church

Contact Information for Business Card

We will likely print through Quillby Printworks. The details of what they need can be found here: http://www.quillbyprint.example/products/business-card

Font styles to use
Other font styles liked:
• Pacifico, Helvetica, Open Sans Regular, Bebas Nue

Colors
0592cd
34a7d8
85cae6
cee9f5
0455a3
3176b5
85acd3
cfdfed

Requirements
Must have
• Sleek, eye catching design
Nice to have
• Rounded Corners, Our social media sites (PB, Snapg and VidStream)

```html
<!DOCTYPE html>
<html lang="en">
<head>
<meta charset="utf-8">
<title>Harlow Creek Church Invite Card</title>
<link rel="stylesheet" href="https://fonts.googleapis.com/css2?family=Open+Sans:wght@400;600;700&family=Cookie&display=swap">
<style>
  :root {
    --brand-blue: #1a6ab7;
    --ink: #111111;
    --paper: #ffffff;
    --stage: #2b2b2b;
    --muted: #9a9a9a;
    --text-grey: #333333;
  }
  * { margin: 0; padding: 0; box-sizing: border-box; }
  html, body { width: 1200px; height: 900px; overflow: hidden; }
  body {
    background: var(--stage);
    font-family: "Open Sans", Helvetica, Arial, sans-serif;
    position: relative;
  }
  .card {
    position: absolute;
    width: 700px;
    height: 400px;
    background: var(--paper);
    border-radius: 28px;
    overflow: hidden;
    box-shadow: 0 14px 30px rgba(0,0,0,.45);
  }
  .brand-name {
    font-family: "Open Sans", Helvetica, Arial, sans-serif;
    font-weight: 700;
    color: var(--ink);
    letter-spacing: .5px;
    line-height: 1;
    white-space: nowrap;
  }

  /* Front */
  .card--front { left: 70px; top: 50px; }
  .welcome-banner {
    position: absolute; left: 90px; top: 70px;
    background: var(--ink); color: var(--paper);
    font-family: "Cookie", cursive;
    font-size: 46px; line-height: 1;
    padding: 6px 26px 8px;
    white-space: nowrap;
  }
  .card--front .brand-name {
    position: absolute; left: 200px; top: 160px; font-size: 36px;
  }
  .social-list {
    position: absolute; left: 200px; top: 240px;
    list-style: none; color: var(--text-grey);
    font-size: 20px; line-height: 30px;
  }
  .social-list li { display: flex; align-items: center; gap: 10px; white-space: nowrap; }
  .social-list .dot {
    width: 16px; height: 16px; background: var(--brand-blue); display: inline-block; flex: none;
  }

  /* Back */
  .card--back { left: 430px; top: 460px; }
  .divider-art { position: absolute; inset: 0; }
  .service-bar {
    position: absolute; left: 0; top: 40px; height: 38px;
    display: flex;
  }
  .service-bar .tab { width: 22px; background: var(--muted); }
  .service-bar .label {
    background: var(--ink); color: var(--paper);
    font-size: 17px; line-height: 38px; padding: 0 14px 0 12px; white-space: nowrap;
  }
  .service-bar .accent { color: var(--brand-blue); font-weight: 700; }
  .card--back .brand-name {
    position: absolute; left: 36px; top: 150px; font-size: 28px;
  }
  .contact {
    position: absolute; right: 28px; top: 150px;
    text-align: right; color: var(--paper);
    font-size: 16px; line-height: 25px;
    white-space: nowrap;
  }
  .contact .person {
    color: var(--brand-blue); font-weight: 700; font-size: 26px; line-height: 40px;
  }
  .contact .web .accent { color: var(--brand-blue); }
  .contact svg { vertical-align: middle; margin-left: 6px; }
</style>
</head>
<body>

<section class="card card--front" aria-label="Invite card front">
  <div class="welcome-banner">We look forward to meeting you</div>
  <div class="brand-name">Harlow Creek Church</div>
  <ul class="social-list">
    <li><span class="dot"></span>plazebook.example/harlowcreekchurch</li>
    <li><span class="dot"></span>snapgrove.example/harlowcreekchurch</li>
    <li><span class="dot"></span>vidstream.example/harlowcreekyouth</li>
  </ul>
</section>

<section class="card card--back" aria-label="Invite card back">
  <svg class="divider-art" width="700" height="400" viewBox="0 0 700 400">
    <path d="M350 400 C 430 300, 430 160, 510 100 C 570 60, 600 25, 610 0 L700 0 L700 400 Z" fill="var(--ink)"/>
    <path d="M350 400 C 430 300, 430 160, 510 100 C 570 60, 600 25, 610 0" fill="none" stroke="var(--brand-blue)" stroke-width="24" stroke-linecap="round"/>
  </svg>
  <div class="service-bar">
    <span class="tab"></span>
    <span class="label"><span class="accent">SERVICE TIMES:</span> Sunday @ <span class="accent">8:30</span> AM &amp; <span class="accent">11:00</span> AM</span>
  </div>
  <div class="brand-name">Harlow Creek Church</div>
  <div class="contact">
    <div class="person">DANIEL REYES</div>
    <div>4827 Marlow</div>
    <div>Avenue Ashvale, ST 00481</div>
    <div>(555) 555-0182<svg width="14" height="14" viewBox="0 0 24 24"><path d="M6.6 10.8a15 15 0 0 0 6.6 6.6l2.2-2.2a1 1 0 0 1 1-.25 11.4 11.4 0 0 0 3.6.6 1 1 0 0 1 1 1V20a1 1 0 0 1-1 1A17 17 0 0 1 3 4a1 1 0 0 1 1-1h3.5a1 1 0 0 1 1 1c0 1.25.2 2.45.6 3.6a1 1 0 0 1-.25 1z" fill="var(--brand-blue)"/></svg></div>
    <div class="web">www.<span class="accent">harlowcreek</span>.org<svg width="14" height="14" viewBox="0 0 24 24"><circle cx="12" cy="12" r="9" fill="none" stroke="var(--brand-blue)" stroke-width="2.5"/><path d="M3 12h18M12 3c3 3 3 15 0 18M12 3c-3 3-3 15 0 18" fill="none" stroke="var(--brand-blue)" stroke-width="2"/></svg></div>
  </div>
</section>

</body>
</html>
```